Coffee Shop needs a fresh new menu

Hi,
I would like a new menu to be designed for our coffee shop.
We display our menu on a television screen, so would need it in a file that would allow us to continue to do so -- I have attached a photo so that you can see our current design, and how it is displayed.

I'd like something that is easy to read, if the design could have a "hipster" feel to it -- we are located at a hospital and University.

I have attached a Word file with what we would like on the menu.

Feel free to contact me if you have any questions.

Thanks,
Tam

Just A4 size will be fine, and no need to include menu 1 and menu 2 - I just put them in as an example of what we already have -- they are our printed menu's. Thanks

Hospital

```html
<!DOCTYPE html>
<html lang="en">
<head>
<meta charset="utf-8">
<title>Canteen Menu</title>
<link rel="stylesheet" href="https://fonts.googleapis.com/css2?family=Lato:wght@700;900&family=Stardos+Stencil:wght@700&display=swap">
<style>
  :root {
    --backdrop: #2b2b2b;
    --sun-top: #f8d200;
    --sun-mid: #fdb000;
    --sun-bottom: #ff8600;
    --menu-red: #cc1128;
    --ink: #241509;
    --band: rgba(255, 240, 170, 0.45);
    --white: #ffffff;
  }
  * { margin: 0; padding: 0; box-sizing: border-box; }
  html, body { width: 1200px; height: 1000px; overflow: hidden; background: var(--backdrop); }
  .menu-board {
    position: absolute; left: 38px; top: 102px; width: 1126px; height: 796px;
    background: linear-gradient(180deg, var(--sun-top) 0%, var(--sun-mid) 50%, var(--sun-bottom) 100%);
    font-family: "Lato", Arial, sans-serif; font-weight: 700; color: var(--ink);
  }
  .frame { position: absolute; left: 0; top: 0; }
  .menu-title {
    position: absolute; left: 0; width: 100%; top: 28px; text-align: center;
    font-family: "Stardos Stencil", "Lato", serif; font-weight: 700;
    font-size: 48px; letter-spacing: 1px; color: var(--menu-red);
  }
  .section-title {
    position: absolute; font-size: 29px; font-weight: 900; color: var(--menu-red); letter-spacing: -0.2px;
  }
  .item-list { position: absolute; list-style: none; width: 440px; }
  .item {
    position: relative; height: 26px; margin-bottom: 5.8px;
    font-size: 20px; line-height: 26px; padding-left: 30px;
  }
  .item:nth-child(odd) {
    background: linear-gradient(90deg, rgba(255,240,170,0) 0%, var(--band) 8%, var(--band) 92%, rgba(255,240,170,0) 100%);
  }
  .item .price { position: absolute; left: 355px; top: 0; }
  .store-note { position: absolute; left: 622px; top: 540px; font-size: 17px; line-height: 23.5px; }
  .social-handle {
    position: absolute; left: 622px; top: 689px; font-size: 18px; font-weight: 900; color: var(--white);
    text-shadow: 0 0 2px var(--menu-red), 0 0 2px var(--menu-red), 0 0 2px var(--menu-red);
  }
  .brand-badge {
    position: absolute; left: 869px; top: 568px; width: 150px; height: 150px; border-radius: 50%;
    background: var(--white); border: 9px solid var(--menu-red);
    display: flex; align-items: center; justify-content: center; text-align: center;
  }
  .brand-name { font-size: 27px; font-weight: 900; line-height: 1.05; color: var(--menu-red); }
</style>
</head>
<body>
<main class="menu-board">
  <svg class="frame" width="1126" height="796" viewBox="0 0 1126 796" aria-hidden="true">
    <g fill="none" stroke="#cc1128" stroke-width="3">
      <polyline points="463,48 47,48 47,756 1077,756 1077,48 659,48"/>
      <polyline points="463,61 31,61 31,743 1092,743 1092,61 659,61"/>
    </g>
  </svg>
  <h1 class="menu-title">MENU</h1>

  <h2 class="section-title" style="left:119px; top:86px;">Something Light:</h2>
  <ul class="item-list" style="left:90px; top:134px;">
    <li class="item">Mixed Yoghurts<span class="price">$5.50</span></li>
    <li class="item">Chia Pudding<span class="price">$5.50</span></li>
    <li class="item">Fruit Salad<span class="price">$5.50</span></li>
    <li class="item">Bircher Muesli<span class="price">$5.50</span></li>
    <li class="item">Protein Balls<span class="price">$4.00</span></li>
    <li class="item">Banana Bread<span class="price">$4.50</span></li>
    <li class="item">Muffins<span class="price">$4.50</span></li>
    <li class="item">Slices<span class="price">$4.00</span></li>
  </ul>

  <h2 class="section-title" style="left:119px; top:399px;">Breakfast Items:</h2>
  <ul class="item-list" style="left:90px; top:444px;">
    <li class="item">Bacon, Egg and Cheese Roll<span class="price">$6.00</span></li>
    <li class="item">Ham and Cheese Toastie<span class="price">$5.00</span></li>
    <li class="item">Cheese and Tomato Toastie<span class="price">$5.00</span></li>
    <li class="item">Ham and Cheese Croissant<span class="price">$6.00</span></li>
    <li class="item">Cheese and Tomato Croissant<span class="price">$5.50</span></li>
    <li class="item">Plain Croissant<span class="price">$3.50</span></li>
    <li class="item">Hash Brown<span class="price">$2.00</span></li>
    <li class="item">2 Piece Toast<span class="price">$3.00</span></li>
    <li class="item">2 Piece Rasin Toast<span class="price">$3.00</span></li>
  </ul>

  <h2 class="section-title" style="left:622px; top:86px;">Hot Food and Sandwiches:</h2>
  <ul class="item-list" style="left:592px; top:134px;">
    <li class="item">Pre Made Sandwiches<span class="price">$6.50</span></li>
    <li class="item">Pre Made Sandwiches<span class="price">$7.50</span></li>
    <li class="item">Pre Made Focaccias<span class="price">$8.50</span></li>
    <li class="item">Wraps<span class="price">$7.50</span></li>
    <li class="item">Vegetarian Salad<span class="price">$7.50</span></li>
    <li class="item">Meat/Seafood Salad<span class="price">$9.50</span></li>
    <li class="item">Hot Chips<span class="price">$4.50</span></li>
    <li class="item">Dim Sim<span class="price">$1.50</span></li>
    <li class="item">Potato Cake<span class="price">$1.50</span></li>
    <li class="item">Plain Hamburger<span class="price">$7.50</span></li>
    <li class="item">Hamburger with the lot<span class="price">$9.00</span></li>
    <li class="item">Chicken Schnitzel Burger<span class="price">$8.50</span></li>
  </ul>

  <p class="store-note">Our Store inside the Hospital<br>Food Court sells:<br>Hot Pies, Assorted Pasta's,<br>Ready-to-go Meals,<br>Quiche, and lots more!</p>
  <p class="social-handle">@wardbitescanteen</p>

  <div class="brand-badge"><span class="brand-name">Ward<br>Bites</span></div>
</main>
</body>
</html>
```